High-end construction company needs a business card design

We need a modern looking business card that draws people in, is memorable and looks so good people will want to sick it on their fridges.
On the first side what is needed are:
Logo
My name - Tomas Verbelk
Title - Managing Director
Website - www.kravel.co.uk
Email - tomas@kravel.co.uk
Telephone - 020 5194 6381
Mobile - 07845319027
On the back side was is needed is a list of all the services we provide:
-Kitchen Renovations
-Bathroom Renovations
-House Renovations
-Garage Conversions
-Extensions
-Loft Conversions
-Conservatories
-Carpentry
-Tiling
-Electrical
-Plumbing & Heating
-Bricklaying
-Landscaping
-Decorating
-Plastering
We would like the colours to be the same shades as on the logo with grey or black for the words.
Target Market(s)
Anyone who needs building work done
Contact Information for Business Card
This business card is for a construction company which strives to deliver excellent service and quality.
The look and feel of the card should represent this.
Requirements
Must have
- On the first side what is needed are:
Logo
My name - Tomas Verbelk
Title - Managing Director
Website - www.kravel.co.uk
Email - tomas@kravel.co.uk
Telephone - 020 5194 6381
Mobile - 07845319027
Nice to have
- Cool looking features

```html
<!DOCTYPE html>
<html lang="en">
<head>
<meta charset="utf-8">
<title>Kravel Construction Ltd – Business Card</title>
<link rel="stylesheet" href="https://fonts.googleapis.com/css2?family=Montserrat:wght@500;600;700;800&display=swap">
<style>
  :root {
    --bg: #eeeeee;
    --card: #ffffff;
    --green: #7cb84a;
    --green-light: #8cc455;
    --green-dark: #4e9a3c;
    --green-deep: #5f9e4e;
    --ink: #3d3d3d;
    --white: #ffffff;
  }
  * { box-sizing: border-box; margin: 0; padding: 0; }
  html, body {
    width: 1200px; height: 1200px; overflow: hidden;
    background: var(--bg);
    font-family: "Montserrat", Arial, sans-serif;
  }
  .canvas { position: relative; width: 1200px; height: 1200px; }
  .card {
    position: absolute; left: 150px; width: 900px; height: 514px;
    background: var(--card); overflow: hidden;
    box-shadow: 0 6px 24px rgba(0,0,0,0.12);
  }
  .card--back { top: 50px; }
  .card--front { top: 630px; }

  /* Back side */
  .back__panel {
    position: absolute; inset: 0;
    background: linear-gradient(135deg, var(--green-light), var(--green) 55%, var(--green-deep));
    clip-path: polygon(0 44%, 100% 30%, 100% 100%, 13% 100%, 19% 62%, 0 62%);
  }
  .back__art {
    position: absolute; right: 40px; bottom: 30px; width: 360px; height: 300px;
    background: radial-gradient(ellipse at 60% 60%, rgba(78,154,60,0.55), rgba(124,184,74,0) 70%);
  }
  .back__brand {
    position: absolute; left: 380px; top: 46px;
    color: var(--green); font-weight: 800; font-size: 24px; letter-spacing: 1px;
    display: flex; align-items: center; gap: 8px;
  }
  .back__brand .mark { width: 12px; height: 12px; background: var(--green); }
  .back__title {
    position: absolute; left: 70px; top: 150px;
    color: var(--green); font-weight: 800; font-size: 62px; letter-spacing: 1px;
  }
  .back__web {
    position: absolute; left: 90px; top: 226px;
    color: var(--white); font-weight: 600; font-size: 26px; letter-spacing: 0.5px;
  }
  .services {
    position: absolute; left: 200px; top: 286px;
    list-style: none;
    display: grid;
    grid-template-columns: 240px 190px 200px;
    grid-template-rows: repeat(5, 36px);
    grid-auto-flow: column;
    column-gap: 24px;
    color: var(--white); font-weight: 700; font-size: 14px; letter-spacing: 0.4px;
    text-transform: uppercase;
  }
  .services li { line-height: 36px; white-space: nowrap; }

  /* Front side */
  .front__brand {
    position: absolute; left: 70px; top: 190px; width: 320px;
    color: var(--green); font-weight: 800; text-align: center;
  }
  .front__brand .name { font-size: 70px; letter-spacing: 3px; line-height: 1; }
  .front__brand .sub { font-size: 17px; letter-spacing: 3.5px; margin-top: 8px; }
  .front__divider {
    position: absolute; left: 450px; top: 130px; width: 3px; height: 260px;
    background: var(--green-dark);
  }
  .contact { position: absolute; left: 500px; top: 160px; }
  .contact__name { color: var(--green-light); font-weight: 800; font-size: 26px; letter-spacing: 1.5px; text-transform: uppercase; }
  .contact__role { color: var(--ink); font-weight: 700; font-size: 15px; letter-spacing: 2px; text-transform: uppercase; margin-top: 4px; }
  .contact__list { list-style: none; margin-top: 30px; font-weight: 600; font-size: 21px; line-height: 34px; }
  .contact__list .web { color: var(--green-light); }
  .contact__list .tel { color: var(--green-dark); }
</style>
</head>
<body>
<main class="canvas">

  <section class="card card--back" aria-label="Back of business card">
    <div class="back__panel"></div>
    <div class="back__art" role="img" aria-label="Faint excavator arm illustration"></div>
    <div class="back__brand"><span class="mark"></span>KRAVEL</div>
    <h2 class="back__title">SERVICES</h2>
    <p class="back__web">www.kravel.co.uk</p>
    <ul class="services">
      <li>Kitchen Renovations</li>
      <li>Bathroom Renovations</li>
      <li>House Renovations</li>
      <li>Garage Conversions</li>
      <li>Extensions</li>
      <li>Loft Conversions</li>
      <li>Conservatories</li>
      <li>Carpentry</li>
      <li>Tiling</li>
      <li>Electrical</li>
      <li>Plumbing &amp; Heating</li>
      <li>Bricklaying</li>
      <li>Landscaping</li>
      <li>Decorating</li>
      <li>Plastering</li>
    </ul>
  </section>

  <section class="card card--front" aria-label="Front of business card">
    <div class="front__brand">
      <div class="name">KRAVEL</div>
      <div class="sub">CONSTRUCTION LTD</div>
    </div>
    <div class="front__divider"></div>
    <div class="contact">
      <p class="contact__name">Tomas Verbelk</p>
      <p class="contact__role">Managing Director</p>
      <ul class="contact__list">
        <li class="web">www.kravel.co.uk</li>
        <li class="web">tomas@kravel.co.uk</li>
        <li class="tel">020 5194 6381</li>
        <li class="tel">07845319027</li>
      </ul>
    </div>
  </section>

</main>
</body>
</html>
```